Diverse business needs a corporate identity system

Brantow Fielding Holdings Limited is a well established family owned and run business operating in Port Moresby, Papua New Guinea since 1989. As part of taking the business to the next level, we are redoing our branding/corporate identity.

We currently carry out two core business activities servicing corporate clients in the commercial and industrial sectors:
1. Electrical - new installations and maintenance work
2. Construction - mostly commercial & industrial, some residential

We are looking to add the following business activities in near future:
1. IT consulting
2. Property development - business/industrial park, residential complexes, low cost housing
3. Retail of hardware, construction supplies and flat pack furniture & kitchens

We have just completed our logo design here on SketchHarbor and now wanting to design business card and stationery based on our new logo (attached).

Deliverables are:
1. Business card - double sided
2. Letterhead A4

Details to go on the card:
Name: Marcus Trevane
Title: Director
Email: marcus.trevane@brantowfield.com
Tel: +675 3147720, +675 3148815
Office: Section 17 Lot 48, Waravu Light Industrial Area, Port Moresby, Papua New Guinea
Postal: PO Box 419, Waravu, NCD, Papua New Guinea
Website: brantowfield.com

Our services can be listed somewhere on the card:
Electrical, Construction, Property Development, IT Consulting

Details to go on the letterhead:
Brantow Fielding Holdings Ltd.
PO Box 419, Waravu, NCD, Papua New Guinea
Fax: +675 3146603
Email: info@brantowfield.com

For inspiration, I have uploaded some images of business cards we like.

Would be good if the same/similar business card design could be printed both economically (e.g. full coloured both sides, matte card stock) for majority of staff and upscaled to use premium features such as letter pressed, foil etc for use by executives. Otherwise, please provide two separate designs.

Logo text font is nexa bold freefont - please use something from nexa family or another font type that complements it.

Reason: Few designs were submitted. Most were clearly from ready to use templates. No designs really stand out for us at the moment. So we have decided to narrow the focus to just business card and A4 letterhead. And also revised the brief to be completely open to hopefully invite more creative designs.

I have updated the brief to be a lot less restrictive to try and get more creative designs. Also uploaded more images of premium business cards for inspiration.

Industry/Entity Type

Construction

Requirements
Must have
• All designs must conform to printolane specifications. Refer to and download appropriate work file templates from http://www.printolane.com.au/pl/ns/files/UploadResources.aspx?GP=1%2F9%2F2014+12%3A53%3A21+AM&GPS=5829104463&GNF=1&selectedTab=0.
Should not have
• No QR codes and social media links.

```html
<!DOCTYPE html>
<html lang="en">
<head>
<meta charset="utf-8">
<title>Brantow Fielding — Business Card</title>
<link rel="stylesheet" href="https://fonts.googleapis.com/css2?family=Roboto:wght@400;500;700&display=swap">
<style>
  :root {
    --brand-red: #d9261c;
    --text-grey: #555555;
    --icon-grey: #8a8a8a;
    --card-white: #ffffff;
    --card-fade: #e6e6e6;
    --backdrop: #ebe8e4;
  }
  * { margin: 0; padding: 0; box-sizing: border-box; }
  html, body {
    width: 1200px; height: 803px; overflow: hidden;
    background: var(--backdrop);
    font-family: "Roboto", Arial, sans-serif;
  }
  .stage {
    position: relative; width: 1200px; height: 803px;
    display: flex; align-items: center; justify-content: center; gap: 60px;
  }
  .card {
    position: relative; width: 520px; height: 297px;
    background: var(--card-white);
    box-shadow: 0 6px 18px rgba(0,0,0,0.18);
    overflow: hidden;
  }
  .wordmark {
    display: flex; align-items: center; gap: 9px;
    color: var(--brand-red); font-weight: 700; white-space: nowrap;
  }
  .wordmark-dot {
    border-radius: 50%; background: var(--brand-red); flex: none;
  }

  /* front */
  .card-front {
    background: linear-gradient(180deg, var(--card-white) 30%, var(--card-fade) 100%);
  }
  .card-front .top-band {
    position: absolute; left: 0; top: 0; width: 100%; height: 28px;
    background: var(--brand-red);
  }
  .card-front .wordmark {
    position: absolute; left: 0; right: 0; top: 102px;
    justify-content: center; font-size: 30px;
  }
  .card-front .wordmark-dot { width: 28px; height: 28px; }
  .card-front .services {
    position: absolute; left: 0; right: 0; top: 206px;
    text-align: center; font-size: 14px; font-weight: 500;
    color: var(--brand-red); letter-spacing: 0.2px;
  }
  .services .divider { color: #b0b0b0; margin: 0 4px; }

  /* back */
  .card-back .wordmark {
    position: absolute; left: 36px; top: 112px; font-size: 20px;
  }
  .card-back .wordmark-dot { width: 20px; height: 20px; }
  .contact {
    position: absolute; left: 300px; top: 30px;
    font-size: 12px; color: var(--text-grey); line-height: 17px;
  }
  .contact .rule {
    width: 16px; height: 2px; background: var(--brand-red);
    margin: 8px 0 8px 12px;
  }
  .contact-row { display: flex; align-items: center; gap: 8px; }
  .contact-row svg { width: 12px; height: 12px; flex: none; fill: var(--icon-grey); }
  .address { padding-left: 0; }
  .bottom-band {
    position: absolute; left: 0; bottom: 0; width: 100%; height: 42px;
    background: var(--brand-red);
    display: flex; align-items: center; justify-content: center;
    color: #ffffff; font-size: 13px; letter-spacing: 0.2px;
  }
  .bottom-band .divider { margin: 0 4px; opacity: 0.8; }
</style>
</head>
<body>
<main class="stage">

  <section class="card card-front" aria-label="Business card front">
    <div class="top-band"></div>
    <div class="wordmark"><span class="wordmark-dot"></span>Brantow Fielding</div>
    <p class="services">Electrical<span class="divider">|</span>Construction<span class="divider">|</span>Property Development<span class="divider">|</span>IT Consulting</p>
  </section>

  <section class="card card-back" aria-label="Business card back">
    <div class="wordmark"><span class="wordmark-dot"></span>Brantow Fielding</div>
    <div class="contact">
      <p class="address">17 Waravu Road<br>Port Moresby, NCD 111</p>
      <div class="rule"></div>
      <p class="contact-row">
        <svg viewBox="0 0 12 12" aria-hidden="true"><path d="M2.4 1l2 2-1 1.3a7 7 0 0 0 4.3 4.3L9 7.6l2 2-1.3 1.4C5.5 11 1 6.5 1 2.3z"/></svg>
        +675.3147.720
      </p>
      <p class="contact-row">
        <svg viewBox="0 0 12 12" aria-hidden="true"><path d="M3 1h6v3H3zM1 5h10v5H9V8H3v2H1zM3 9h6v2H3z"/></svg>
        +675.3148.815
      </p>
      <div class="rule"></div>
      <p class="contact-row">
        <svg viewBox="0 0 12 12" aria-hidden="true"><path d="M1 2.5h10v7H1zM1.6 3l4.4 3.4L10.4 3v1L6 7.4 1.6 4z" fill-rule="evenodd"/></svg>
        marcus@brantowfield.com
      </p>
      <p class="contact-row">
        <svg viewBox="0 0 12 12" aria-hidden="true"><circle cx="6" cy="6" r="5"/><path d="M1 6h10M6 1c-2 2.6-2 7.4 0 10M6 1c2 2.6 2 7.4 0 10" stroke="#ffffff" stroke-width="0.8" fill="none"/></svg>
        brantowfield.com
      </p>
    </div>
    <div class="bottom-band">Electrical<span class="divider">|</span>Construction<span class="divider">|</span>Property Development<span class="divider">|</span>IT Consulting</div>
  </section>

</main>
</body>
</html>
```